Flyer für Natur- und Chiropraxis
Zielgruppe
Natur- und Chiropraxis. (Berufsbild Heilpraktiker)
Ganzheitliche Chiropraktik und manuelle Gelenktherapie.
Patienten mit chronischen oder akuten Beschwerden des Halte- und Bewegungsapparates (z.b. Migräne+Spannungskopfschmerzen, Muskelkettendysbalancen, Bandscheibenvorfälle)
HWS und Atlastherapie (Bei Tinnitus, Schwindel, Kopfschmerzen)
Naturheilkunde und Vitalstoffinfusionen (Bei LongCovid und chronischem Erschöpfungssyndrom)
Extrakorporale Stoßwellentherapie ( Bei Fersensporn, Kalkschulter, Sehnenansatzentzündungen.)
Nebensächlich=Neuraltherapie, Extensionstherapie, Wärmetherapie, Magnetfeldtherapie, biologische Arthrosebehandlung, Dry-Needling Therapie.
Aufgabenstellung
Bitte das Heilmittelwerbegesetz beachten!
Geplanter start der Praxis 17.04.23
Adresse der Praxis= Lindenweg 7, 57312 Wiesental. Tel. 06543/73945

```html
<!DOCTYPE html>
<html lang="de">
<head>
<meta charset="utf-8">
<title>Flyer Natur- und Chiropraxis</title>
<link rel="stylesheet" href="https://fonts.googleapis.com/css2?family=Montserrat:wght@500;700;800&family=Poiret+One&family=Prata&display=swap">
<style>
:root{
  --stage:#dedede;
  --paper:#ececec;
  --white:#f7f7f7;
  --gold:#94815b;
  --slate:#b8c2c3;
  --ink:#2f2f2f;
  --dark:#3e3e3e;
  --muted:#6b6b6b;
}
*{box-sizing:border-box;margin:0;padding:0}
html,body{width:1200px;height:900px;overflow:hidden}
body{background:var(--stage);font-family:"Poiret One",sans-serif;color:var(--ink);position:relative}
.spread{position:absolute;top:140px;width:540px;height:620px;display:flex;box-shadow:0 10px 30px rgba(0,0,0,.18)}
.spread--outside{left:45px}
.spread--inside{left:615px}
.panel{position:relative;width:270px;height:620px;overflow:hidden}
.panel--back,.panel--cover{background:var(--paper)}
.photo{position:absolute}
/* back panel */
.back-photo{left:0;top:0;width:270px;height:220px;background:linear-gradient(135deg,#c9c4c0 0%,#8c8378 45%,#5d6158 70%,#d5d2cf 100%)}
.house{position:absolute;left:0;top:160px;width:270px;height:460px}
.welcome{position:absolute;left:20px;top:240px;width:230px;text-align:center;font-size:17px;line-height:1.4}
.badge{position:absolute;left:30px;top:340px;width:100px;height:140px;background:#fff;border-top:12px solid #23378a;border-bottom:12px solid #23378a;box-shadow:4px 4px 0 #fff,5px 5px 8px rgba(0,0,0,.15)}
.badge::after{content:"";position:absolute;left:25px;top:30px;width:50px;height:50px;border-radius:50%;background:#c9c9c9}
.mark-circle{position:absolute;left:170px;top:390px;width:52px;height:52px;border-radius:50%;border:2px solid var(--slate);background:#fff}
.back-name{position:absolute;left:0;top:515px;width:270px;text-align:center;font-family:"Prata",serif;font-size:13px;color:var(--ink)}
.contact-bar{position:absolute;left:0;bottom:0;width:270px;height:58px;background:var(--slate);display:flex;align-items:center;justify-content:space-around;padding:0 10px;font-family:"Montserrat",sans-serif;font-size:9.5px;font-style:italic;color:var(--ink)}
.contact{display:flex;align-items:center;gap:5px;line-height:1.5}
/* cover */
.brand{position:absolute;left:22px;top:20px;display:flex;align-items:center;gap:10px}
.brand-circle{width:40px;height:40px;border-radius:50%;border:2px solid var(--slate);background:#fff;flex:none}
.brand-name{font-size:15px;line-height:1.25;color:var(--gold)}
.headline{position:absolute;left:0;top:76px;width:270px;text-align:center;font-family:"Montserrat",sans-serif;font-weight:800;font-size:24px;letter-spacing:-.5px;color:var(--ink)}
.subline{position:absolute;left:0;top:112px;width:270px;text-align:center;font-size:19px}
.profession{position:absolute;left:0;top:140px;width:270px;text-align:center;font-family:"Montserrat",sans-serif;font-size:7px;font-style:italic;font-weight:500;color:var(--gold)}
.spine-photo{left:100px;top:168px;width:150px;height:300px;border-radius:22px;background:linear-gradient(180deg,#e6e6e6,#d9d3c8 50%,#e9e9e9)}
.massage-photo{left:38px;top:288px;width:90px;height:98px;border-radius:8px;background:linear-gradient(135deg,#d8cfc6,#a2836a 55%,#4a3c34)}
.rule{position:absolute;left:28px;top:260px;width:1px;height:210px;background:var(--ink)}
.date{position:absolute;left:36px;top:392px;font-family:"Prata",serif;font-size:26px;line-height:.95;letter-spacing:2px;color:var(--ink)}
.claim{position:absolute;left:20px;top:478px;width:180px;height:76px;background:var(--slate);border-radius:0 22px 22px 0;display:flex;align-items:center;justify-content:center;text-align:center;font-size:14px;line-height:1.35;padding:6px}
.cta{position:absolute;left:110px;top:564px;width:136px;height:36px;border-radius:12px;background:var(--dark);color:var(--gold);font-family:"Montserrat",sans-serif;font-size:7px;line-height:1.35;display:flex;align-items:center;justify-content:center;text-align:center}
/* inside left */
.panel--offers{background:var(--gold);color:#fff}
.offers-title{position:absolute;left:0;top:22px;width:270px;text-align:center;font-family:"Prata",serif;font-size:21px;line-height:1.25}
.offers-text{position:absolute;left:14px;top:90px;width:242px;text-align:center;font-size:12px;line-height:1.5;letter-spacing:.3px}
.photo-band{position:absolute;left:0;top:232px;width:270px;height:250px;background:var(--white)}
.headache-frame{position:absolute;left:60px;top:250px;width:196px;height:144px;background:#fff}
.headache-photo{left:50px;top:240px;width:190px;height:140px;background:linear-gradient(135deg,#d9d8d4,#a0765c 50%,#8f2a2c)}
.dark-frame{position:absolute;left:40px;top:350px;width:120px;height:140px;background:#3e3e3e}
.sitting-photo{left:20px;top:340px;width:125px;height:135px;background:linear-gradient(135deg,#e2e0dc,#b19b86 50%,#5c5a66)}
.hws-title{position:absolute;left:0;top:550px;width:270px;text-align:center;font-size:19px}
.hws-note{position:absolute;left:0;top:578px;width:270px;text-align:center;font-family:"Prata",serif;font-size:6.5px;letter-spacing:.6px}
/* inside right */
.panel--more{background:var(--white)}
.more-title{position:absolute;left:14px;top:16px;width:220px;text-align:center;font-family:"Prata",serif;font-size:10.5px}
.arrow{position:absolute;left:190px;top:34px}
.more-text{position:absolute;left:10px;top:95px;width:200px;text-align:center;font-size:12.5px;line-height:1.4}
.gold-block{position:absolute;left:0;top:250px;width:200px;height:230px;background:var(--gold)}
.sleep-photo{left:40px;top:232px;width:170px;height:150px;background:linear-gradient(135deg,#c9c6c1,#8d8a85 45%,#f0efed 70%,#555)}
.hand-photo{left:10px;top:350px;width:130px;height:120px;background:linear-gradient(135deg,#a33a8c,#c99a7e 40%,#e4c1a8)}
.white-frame{position:absolute;left:30px;top:340px;width:125px;height:130px;background:#fff}
.shock-text{position:absolute;left:6px;top:500px;width:210px;text-align:center;font-size:12.5px;line-height:1.4}
.side-strip{position:absolute;right:0;top:60px;width:44px;height:560px;background:var(--gold)}
.side-text{position:absolute;left:226px;top:70px;width:44px;height:540px;writing-mode:vertical-rl;font-family:"Montserrat",sans-serif;font-size:8.5px;line-height:1.6;color:#fff;padding:6px 0 0 0;display:flex;align-items:center}
</style>
</head>
<body>

<section class="spread spread--outside">
  <article class="panel panel--back">
    <div class="photo back-photo" role="img" aria-label="Foto: Therapeut behandelt die Schulter einer Patientin"></div>
    <svg class="house" viewBox="0 0 270 460" aria-hidden="true">
      <defs><linearGradient id="houseFill" x1="0" y1="0" x2="1" y2="1"><stop offset="0" stop-color="#f2f2f2"/><stop offset="1" stop-color="#cfcfcf"/></linearGradient></defs>
      <polygon points="0,60 135,0 270,60 270,460 0,460" fill="url(#houseFill)"/>
    </svg>
    <p class="welcome">Ab dem 17.4.2023 heiße ich Sie herzlich willkommen in meiner neuen Praxis</p>
    <div class="badge" aria-label="Zertifikat"></div>
    <div class="mark-circle" aria-hidden="true"></div>
    <p class="back-name">Dr. med. Jonas Wernhoff</p>
    <div class="contact-bar">
      <div class="contact">
        <svg width="16" height="22" viewBox="0 0 16 22" aria-hidden="true"><path d="M8 1C4 1 1.5 4 1.5 7.5 1.5 12 8 20 8 20s6.5-8 6.5-12.5C14.5 4 12 1 8 1z" fill="none" stroke="#6b6b6b" stroke-width="1.2"/><circle cx="8" cy="7.5" r="2.3" fill="none" stroke="#6b6b6b" stroke-width="1.2"/></svg>
        <span>Lindenweg 7<br>57312 Wiesental</span>
      </div>
      <div class="contact">
        <svg width="16" height="16" viewBox="0 0 24 24" aria-hidden="true"><path d="M6.6 10.8c1.4 2.8 3.8 5.1 6.6 6.6l2.2-2.2c.3-.3.7-.4 1-.2 1.1.4 2.3.6 3.6.6.6 0 1 .4 1 1V20c0 .6-.4 1-1 1C10.6 21 3 13.4 3 4c0-.6.4-1 1-1h3.5c.6 0 1 .4 1 1 0 1.3.2 2.5.6 3.6.1.3 0 .7-.2 1z" fill="none" stroke="#6b6b6b" stroke-width="1.4"/></svg>
        <span>06543/73945</span>
      </div>
    </div>
  </article>

  <article class="panel panel--cover">
    <div class="brand">
      <span class="brand-circle" aria-hidden="true"></span>
      <span class="brand-name">Dr. med.<br>Jonas Wernhoff</span>
    </div>
    <h1 class="headline">NEUERÖFFNUNG</h1>
    <p class="subline">Natur und Chiropraxis</p>
    <p class="profession">(Berufsbild Heilpraktiker)</p>
    <div class="photo spine-photo" role="img" aria-label="Abbildung: Modell einer menschlichen Wirbelsäule"></div>
    <div class="rule" aria-hidden="true"></div>
    <div class="photo massage-photo" role="img" aria-label="Foto: Rückenmassage einer liegenden Patientin"></div>
    <p class="date">17<br>APRIL<br>2023</p>
    <p class="claim">Ganzheitliche Chiropraktik und manuelle Gelenktherapie.</p>
    <p class="cta">Unsere Therapieangebote<br>siehe Innenteil</p>
  </article>
</section>

<section class="spread spread--inside">
  <article class="panel panel--offers">
    <h2 class="offers-title">Unsere<br>Therapieangebote</h2>
    <p class="offers-text">Patienten mit chronischen oder akuten Beschwerden des Halte- und Bewegungsapparates (z.B. Migräne+Spannungskopfschmerzen, Muskelkettendysbalancen, Bandscheibenvorfälle)</p>
    <div class="photo-band" aria-hidden="true"></div>
    <div class="headache-frame" aria-hidden="true"></div>
    <div class="photo headache-photo" role="img" aria-label="Foto: Frau mit Kopfschmerzen"></div>
    <div class="dark-frame" aria-hidden="true"></div>
    <div class="photo sitting-photo" role="img" aria-label="Foto: Mann sitzt mit Schmerzen auf dem Bett"></div>
    <p class="hws-title">HWS und Atlastherapie</p>
    <p class="hws-note">(Bei Tinnitus, Schwindel, Kopfschmerzen)</p>
  </article>

  <article class="panel panel--more">
    <h3 class="more-title">Weitere Therapienebenangebote</h3>
    <svg class="arrow" width="30" height="44" viewBox="0 0 30 44" aria-hidden="true"><path d="M12 2C2 12 4 30 22 36" fill="none" stroke="#555" stroke-width="3"/><path d="M16 28l8 8-10 4" fill="none" stroke="#555" stroke-width="3"/></svg>
    <p class="more-text">Naturheilkunde und Vitalstoffinfusionen (Bei LongCovid und chronischem Erschöpfungssyndrom)</p>
    <div class="gold-block" aria-hidden="true"></div>
    <div class="photo sleep-photo" role="img" aria-label="Foto: erschöpfte Frau liegt am Tisch"></div>
    <div class="white-frame" aria-hidden="true"></div>
    <div class="photo hand-photo" role="img" aria-label="Foto: Hand auf einer schmerzenden Schulter"></div>
    <p class="shock-text">Extrakorporale Stoßwellentherapie (Bei Fersensporn, Kalkschulter, Sehnenansatzentzündungen.)</p>
    <div class="side-strip" aria-hidden="true"></div>
    <p class="side-text">Neuraltherapie, Extensionstherapie, Wärmetherapie, Magnetfeldtherapie, biologische Arthrosebehandlung, Dry-Needling Therapie.</p>
  </article>
</section>

</body>
</html>
```